nine-parts.com

We are a small dollar lending company that will revolutionize the industry. We will do this by being completely transparent, fee free, etc and an interest rate that normal people can afford to pay. Over 10X less than our competition. We only allow our members to pay bills " bills paid fast", within 72 hours. Payday loans typically charge from 390%-600% with a terrible payback structure. We charge 36%, period, with a payback structure over 12 months. Our site will be very simple and easy to use but elegant at the same time. We do not want the site to be too busy, less is more and easier. We will have; Home, The Story, Why 9parts.com, Are you eligible? Members, Clients. To become a member you have to be referred by a current client of 9parts.com. A lot of the busy stuff will be saved for the Members and Clients sections. The feel must be elegant, easy to use and very simple to understand. I am looking for the green, white and black combinations of colors, very similar to my logo that was designed by Pixelmoor.

```html
<!DOCTYPE html>
<html lang="en">
<head>
<meta charset="utf-8">
<title>nine-parts.com</title>
<link href="https://fonts.googleapis.com/css2?family=Open+Sans:wght@400;600;700;800&display=swap" rel="stylesheet">
<style>
:root{
  --green:#5cb82e;
  --green-dark:#3f8f1c;
  --green-deep:#2e6e12;
  --green-light:#8fd35c;
  --ink:#2b2b2b;
  --text:#6a6a6a;
  --muted:#9a9a9a;
  --line:#e2e2e2;
  --navy:#1f2b3a;
  --navy-deep:#172230;
  --white:#ffffff;
  --paper:#f6f7f5;
}
*{box-sizing:border-box;margin:0;padding:0}
html,body{width:1200px;height:2480px;overflow:hidden}
body{font-family:"Open Sans",Arial,sans-serif;color:var(--text);background:var(--white);font-size:13px;line-height:1.6}
.wrap{width:900px;margin:0 auto;position:relative}
h2.section-title{font-size:30px;font-weight:700;color:var(--ink);text-align:center;line-height:1.2}
.section-sub{text-align:center;font-size:14px;color:var(--muted);margin-top:10px}

/* header */
.site-header{height:80px;background:var(--white)}
.site-header .wrap{display:flex;justify-content:space-between;align-items:center;height:80px}
.brand{display:flex;align-items:center;gap:10px}
.brand-mark{width:40px;height:40px;border-radius:50%;background:var(--green)}
.brand-name{font-size:24px;font-weight:800;color:var(--ink)}
.header-tools{text-align:right}
.header-tools .row{display:flex;gap:8px;justify-content:flex-end;align-items:center}
.login-pill{background:var(--ink);color:var(--white);font-size:11px;padding:4px 14px;border-radius:3px}
.search-box{width:120px;height:24px;border:1px solid var(--line);border-radius:3px;font-size:11px;color:var(--muted);padding:3px 8px}
.phone-line{margin-top:8px;font-size:12px;color:var(--muted)}
.phone-line strong{color:var(--ink);font-size:15px}

/* nav */
.main-nav{height:32px;background:var(--green)}
.main-nav ul{list-style:none;display:flex;height:32px;align-items:center}
.main-nav li{color:var(--white);font-size:11px;font-weight:700;padding:0 18px;height:32px;line-height:32px}
.main-nav li.active{background:var(--green-dark)}

/* hero */
.hero{height:308px;position:relative;background:linear-gradient(90deg,#b9c7cf 0%,#d6dee2 45%,#e8ecee 70%,#c3cdd3 100%)}
.hero-photo{position:absolute;inset:0}
.hero-copy{position:absolute;left:0;right:0;top:108px;text-align:center}
.hero-copy h1{font-size:30px;font-weight:800;color:var(--white);line-height:1.25;text-shadow:0 1px 3px rgba(0,0,0,.25)}
.btn{display:inline-block;background:var(--green);color:var(--white);font-weight:700;font-size:12px;padding:10px 26px;border-radius:3px}
.hero-copy .btn{margin-top:20px}

/* about */
.about{height:540px;padding-top:52px}
.about .what{text-align:center;font-size:13px;color:var(--ink);margin-top:22px;font-weight:600}
.cards{display:flex;gap:30px;margin-top:20px}
.card{flex:1}
.card-photo{height:168px;border-radius:2px}
.card h3{font-size:13px;font-weight:700;color:var(--ink);margin-top:16px}
.card p{font-size:11.5px;margin-top:6px;line-height:1.6}
.read-more{display:block;margin-top:12px;color:var(--ink);font-weight:600;font-size:12px}

/* bills */
.bills{height:440px;background:linear-gradient(135deg,var(--green-light) 0%,var(--green) 45%,var(--green-dark) 100%);padding-top:44px;color:var(--white)}
.bills h2.section-title{color:var(--white)}
.bills .section-sub{color:#eaf7df}
.bills-body{display:flex;gap:40px;margin-top:34px}
.bills-text{flex:1.1}
.bills-text h3{font-size:17px;font-weight:600;color:var(--white)}
.bills-text p{font-size:11.5px;margin-top:10px;color:#f1fbe9;line-height:1.6}
.bill-list{list-style:none;display:grid;grid-template-columns:repeat(3,120px);gap:4px 10px;margin-top:16px}
.bill-list li{font-size:11px;font-weight:700;display:flex;align-items:center;gap:6px}
.bills-photo{flex:1;height:210px;border:6px solid var(--white);background:linear-gradient(160deg,#dfe7e2,#b9c9bf);margin-top:10px}

/* why */
.why{height:700px;padding-top:54px}
.why-body{display:flex;gap:50px;margin-top:40px}
.calc{flex:1}
.calc h3,.why-copy h3{font-size:15px;font-weight:700;color:var(--green-dark)}
.field{display:flex;align-items:center;margin-top:18px;font-size:12px;color:var(--ink)}
.field label{width:170px}
.field .input{width:110px;height:26px;border:1px solid var(--line);border-radius:2px}
.field .unit{margin-left:10px;color:var(--muted);font-size:11px}
.calc .note{font-size:10.5px;color:var(--muted);margin-top:22px;display:inline-block;width:190px}
.calc .btn{background:var(--green-deep);margin-left:20px;vertical-align:top;margin-top:16px}
.why-copy{flex:1.1}
.why-copy h3{color:var(--green-dark);font-size:17px;line-height:1.35}
.why-copy p{font-size:11.5px;margin-top:14px;line-height:1.65}

/* clients & news */
.clients-news{height:280px}
.clients-news .wrap{display:flex;gap:60px}
.clients,.news{flex:1}
.clients h2,.news h2{font-size:20px;font-weight:700;color:var(--ink)}
.client-grid{display:grid;grid-template-columns:repeat(3,1fr);gap:22px 16px;margin-top:26px}
.client{display:flex;align-items:center;gap:8px;font-size:13px;font-weight:700;color:var(--green-dark)}
.client .dot{width:22px;height:22px;border-radius:50%;background:var(--green)}
.news-item{margin-top:20px;font-size:11.5px}
.news-item h4{font-size:12.5px;color:var(--ink);font-weight:600}
.news-meta{display:flex;gap:14px;color:var(--muted);font-size:11px;margin-top:4px}
.news-meta span{display:flex;align-items:center;gap:4px}

/* footer */
.site-footer{height:100px;background:var(--navy);color:#aab4c0}
.footer-cols{display:flex;gap:30px;padding-top:14px;height:74px}
.footer-col{flex:1;font-size:10.5px;line-height:1.5}
.footer-col h5{color:var(--white);font-size:11px;font-weight:700;margin-bottom:4px}
.subscribe{display:flex;margin-top:2px}
.subscribe .input{flex:1;height:22px;background:var(--white);border-radius:2px 0 0 2px;color:var(--muted);font-size:10px;padding:3px 6px}
.subscribe .go{background:var(--green);color:var(--white);font-size:10px;font-weight:700;padding:3px 10px;border-radius:0 2px 2px 0}
.socials{display:flex;gap:6px;margin-top:6px}
.socials span{width:14px;height:14px;border-radius:50%;background:#3b4a5c}
.copyright{height:26px;background:var(--navy-deep);font-size:10px;text-align:center;line-height:26px;color:#8592a1}
</style>
</head>
<body>

<header class="site-header">
  <div class="wrap">
    <div class="brand"><span class="brand-mark"></span><span class="brand-name">9parts.com</span></div>
    <div class="header-tools">
      <div class="row"><span class="login-pill">Member's Login</span><span class="search-box">Search</span></div>
      <div class="phone-line">Contact us today toll free: <strong>1-800-555-0190</strong></div>
    </div>
  </div>
</header>

<nav class="main-nav">
  <div class="wrap">
    <ul>
      <li class="active">HOME</li><li>ABOUT US</li><li>BILLS PAID FAST</li><li>ARE YOU ELIGIBLE</li><li>WHY 9PARTS.COM</li><li>CONTACT US</li>
    </ul>
  </div>
</nav>

<section class="hero">
  <div class="hero-photo" role="img" aria-label="Smiling businessman in a bright office, softly blurred background"></div>
  <div class="hero-copy">
    <h1>LOREM IPSUM DOLOR SIT AMET<br>CONSECTETUR ADIPISCING ELIT</h1>
    <span class="btn">GET STARTED</span>
  </div>
</section>

<section class="about">
  <div class="wrap">
    <h2 class="section-title">About nine-parts.com</h2>
    <p class="section-sub">Lorem ipsum dolor sit amet, consectetur adipiscing elit, sed do eiusmod<br>tempor incididunt ut labore et dolore magna aliqua.</p>
    <p class="what">What We Do</p>
    <div class="cards">
      <article class="card">
        <div class="card-photo" role="img" aria-label="Couple meeting a loan adviser at a desk" style="background:linear-gradient(150deg,#d9d2c6,#a99a86)"></div>
        <h3>HOME LOANS</h3>
        <p>Sed ut perspiciatis unde omnis iste natus error sit voluptatem accusantium doloremque laudantium, totam rem aperiam eaque ipsa quae ab illo inventore veritatis.</p>
        <span class="read-more">Read More ›</span>
      </article>
      <article class="card">
        <div class="card-photo" role="img" aria-label="Business team shaking hands across a table" style="background:linear-gradient(150deg,#c9d3da,#7f8f9c)"></div>
        <h3>BUSINESS LOANS</h3>
        <p>Nemo enim ipsam voluptatem quia voluptas sit aspernatur aut odit aut fugit, sed quia consequuntur magni dolores eos qui ratione voluptatem sequi nesciunt.</p>
        <span class="read-more">Read More ›</span>
      </article>
      <article class="card">
        <div class="card-photo" role="img" aria-label="Family standing in front of their new house" style="background:linear-gradient(150deg,#dfe3d3,#98a57c)"></div>
        <h3>LOANS AGAINST PROPERTY</h3>
        <p>Neque porro quisquam est, qui dolorem ipsum quia dolor sit amet, consectetur, adipisci velit, sed quia non numquam eius modi tempora incidunt ut labore.</p>
        <span class="read-more">Read More ›</span>
      </article>
    </div>
  </div>
</section>

<section class="bills">
  <div class="wrap">
    <h2 class="section-title">Bills Paid Fast</h2>
    <p class="section-sub">Join Bills to Pay? Get Them Paid Fast Within 72 Hours</p>
    <div class="bills-body">
      <div class="bills-text">
        <h3>At vero eos et accusamus et iusto odio dignissimos</h3>
        <p>Ducimus qui blanditiis praesentium voluptatum deleniti atque corrupti quos dolores et quas molestias excepturi sint occaecati cupiditate non provident, similique sunt in culpa qui officia deserunt mollitia animi, id est laborum et dolorum fuga.</p>
        <p>Et harum quidem rerum facilis est et expedita distinctio. Nam libero tempore, cum soluta nobis est eligendi optio cumque nihil impedit quo minus id quod maxime placeat facere possimus.</p>
        <ul class="bill-list">
          <li><svg width="11" height="11" viewBox="0 0 12 12"><path d="M2 6.5l2.5 2.5L10 3" fill="none" stroke="#fff" stroke-width="2"/></svg>RENT</li>
          <li><svg width="11" height="11" viewBox="0 0 12 12"><path d="M2 6.5l2.5 2.5L10 3" fill="none" stroke="#fff" stroke-width="2"/></svg>MEDICAL</li>
          <li><svg width="11" height="11" viewBox="0 0 12 12"><path d="M2 6.5l2.5 2.5L10 3" fill="none" stroke="#fff" stroke-width="2"/></svg>UTILITY</li>
          <li><svg width="11" height="11" viewBox="0 0 12 12"><path d="M2 6.5l2.5 2.5L10 3" fill="none" stroke="#fff" stroke-width="2"/></svg>PHONE</li>
          <li><svg width="11" height="11" viewBox="0 0 12 12"><path d="M2 6.5l2.5 2.5L10 3" fill="none" stroke="#fff" stroke-width="2"/></svg>INTERNET</li>
          <li><svg width="11" height="11" viewBox="0 0 12 12"><path d="M2 6.5l2.5 2.5L10 3" fill="none" stroke="#fff" stroke-width="2"/></svg>CAR LOAN</li>
          <li><svg width="11" height="11" viewBox="0 0 12 12"><path d="M2 6.5l2.5 2.5L10 3" fill="none" stroke="#fff" stroke-width="2"/></svg>ELECTRIC</li>
          <li><svg width="11" height="11" viewBox="0 0 12 12"><path d="M2 6.5l2.5 2.5L10 3" fill="none" stroke="#fff" stroke-width="2"/></svg>WATER</li>
          <li><svg width="11" height="11" viewBox="0 0 12 12"><path d="M2 6.5l2.5 2.5L10 3" fill="none" stroke="#fff" stroke-width="2"/></svg>OTHER BILLS</li>
        </ul>
      </div>
      <div class="bills-photo" role="img" aria-label="Woman paying bills on a laptop at her desk"></div>
    </div>
  </div>
</section>

<section class="why">
  <div class="wrap">
    <h2 class="section-title">Why You are Visiting</h2>
    <p class="section-sub">On the other hand, we denounce with righteous indignation<br>and dislike men who are so beguiled and demoralized by the charms.</p>
    <div class="why-body">
      <div class="calc">
        <h3>How Much Do I Have to Payback</h3>
        <div class="field"><label>Enter Amount of Loan</label><span class="input"></span><span class="unit">$</span></div>
        <div class="field"><label>Bill Amount ($100 - $750)</label><span class="input"></span><span class="unit">$</span></div>
        <div class="field"><label># of payments</label><span class="input"></span><span class="unit">Month</span></div>
        <div class="field"><label>Total Fee/Rate</label><span class="input"></span><span class="unit">%</span></div>
        <span class="note">*Select interval number to get actual calculations</span><span class="btn">CALCULATIONS</span>
      </div>
      <div class="why-copy">
        <h3>Once approved you will receive a confirmation number and your creditor will be funded within 72 hours</h3>
        <p>Sed ut perspiciatis unde omnis iste natus error sit voluptatem accusantium doloremque laudantium, totam rem aperiam, eaque ipsa quae ab illo inventore veritatis et quasi architecto beatae vitae dicta sunt explicabo. Nemo enim ipsam voluptatem quia voluptas sit aspernatur aut odit aut fugit.</p>
        <p>Sed quia consequuntur magni dolores eos qui ratione voluptatem sequi nesciunt. Neque porro quisquam est, qui dolorem ipsum quia dolor sit amet, consectetur, adipisci velit, sed quia non numquam eius modi tempora incidunt ut labore et dolore magnam aliquam quaerat voluptatem.</p>
        <p>Ut enim ad minima veniam, quis nostrum exercitationem ullam corporis suscipit laboriosam, nisi ut aliquid ex ea commodi consequatur. Quis autem vel eum iure reprehenderit qui in ea voluptate velit esse quam nihil molestiae consequatur, vel illum qui dolorem eum fugiat quo voluptas nulla pariatur.</p>
      </div>
    </div>
  </div>
</section>

<section class="clients-news">
  <div class="wrap">
    <div class="clients">
      <h2>Our Client</h2>
      <div class="client-grid">
        <div class="client"><span class="dot"></span>Halvern</div>
        <div class="client"><span class="dot"></span>Corvale</div>
        <div class="client"><span class="dot"></span>Stonebay</div>
        <div class="client"><span class="dot"></span>Fenwick</div>
        <div class="client"><span class="dot"></span>Orrin</div>
        <div class="client"><span class="dot"></span>Meridel</div>
      </div>
    </div>
    <div class="news">
      <h2>Latest News</h2>
      <div class="news-item">
        <h4>Lorem ipsum dolor sit amet, consectetur adipiscing elit</h4>
        <div class="news-meta">
          <span><svg width="10" height="10" viewBox="0 0 10 10"><rect x="1" y="2" width="8" height="7" fill="none" stroke="#9a9a9a"/></svg>12 May 2016</span>
          <span><svg width="10" height="10" viewBox="0 0 10 10"><circle cx="5" cy="5" r="4" fill="none" stroke="#9a9a9a"/></svg>4 Comments</span>
        </div>
        <p>At vero eos et accusamus et iusto odio dignissimos ducimus qui blanditiis praesentium voluptatum deleniti atque corrupti.</p>
      </div>
      <div class="news-item">
        <h4>Nam libero tempore cum soluta nobis est eligendi</h4>
        <div class="news-meta">
          <span><svg width="10" height="10" viewBox="0 0 10 10"><rect x="1" y="2" width="8" height="7" fill="none" stroke="#9a9a9a"/></svg>08 May 2016</span>
          <span><svg width="10" height="10" viewBox="0 0 10 10"><circle cx="5" cy="5" r="4" fill="none" stroke="#9a9a9a"/></svg>2 Comments</span>
        </div>
        <p>Temporibus autem quibusdam et aut officiis debitis aut rerum necessitatibus saepe eveniet ut et voluptates repudiandae.</p>
      </div>
    </div>
  </div>
</section>

<footer class="site-footer">
  <div class="wrap">
    <div class="footer-cols">
      <div class="footer-col"><h5>OUR LINK</h5>Home · About Us · Bills Paid Fast<br>Are You Eligible · Contact Us</div>
      <div class="footer-col"><h5>CONTACT INFO</h5>418 Larkmoor Avenue, Suite 9<br>1-800-555-0190 · hello@nine-parts.com</div>
      <div class="footer-col"><h5>LATEST TWITTER</h5>Bills paid fast within 72 hours for members. Learn more today.</div>
      <div class="footer-col"><h5>SUBSCRIBE TO OUR NEWSLETTER</h5>
        <div class="subscribe"><span class="input">Enter email</span><span class="go">SUBSCRIBE</span></div>
        <div class="socials"><span></span><span></span><span></span><span></span></div>
      </div>
    </div>
  </div>
  <div class="copyright">Copyright © nine-parts.com 2016. All Rights Reserved. | Sitemap | Terms &amp; Conditions</div>
</footer>

</body>
</html>
```